Redesign www.KORVADO.ch - Shopify Web-Shop - Storytelling

Redesign of existing Shopify Web-page of KOR-VADO.ch.
Please carefully review both enclosed documents. The annotated notes explain the expected design direction and priorities.

```html
<!DOCTYPE html>
<html lang="en">
<head>
<meta charset="utf-8">
<title>KOR-VADO – Mobile Shop Redesign</title>
<link href="https://fonts.googleapis.com/css2?family=Cormorant+SC:wght@400;500&family=Cormorant+Garamond:ital,wght@0,500;1,400;1,600&family=Jost:wght@400;500;600&display=swap" rel="stylesheet">
<style>
:root{
  --stage:#767676;
  --ink:#4f545b;
  --ink-soft:#6b7077;
  --dark:#55595f;
  --white:#ffffff;
  --paper:#f1f1f1;
  --mist:#f6f9f9;
  --line:#8e9298;
  --chip:#c9cccd;
  --strip:#ececec;
}
*{box-sizing:border-box;margin:0;padding:0}
html,body{width:1200px;height:2339px;overflow:hidden;background:var(--stage)}
.stage{position:absolute;left:0;top:0;width:1322px;height:2576px;transform:scale(0.90772);transform-origin:0 0;font-family:"Jost",sans-serif;color:var(--ink)}
.a{position:absolute}
.screen{position:absolute;width:276px;overflow:hidden}
.screen--shop{left:351px;top:316px;height:2004px;background:var(--white)}
.screen--story{left:706px;top:316px;height:1852px;background:var(--white)}
.heading{position:absolute;left:0;width:276px;text-align:center;font-family:"Cormorant SC",serif;font-weight:500;font-size:21px;letter-spacing:.5px;color:var(--ink)}
.rule{position:absolute;height:1px;background:var(--line)}
.rule::after{content:"";position:absolute;left:50%;top:-2px;width:5px;height:5px;margin-left:-2.5px;background:var(--line);transform:rotate(45deg)}
.copy{position:absolute;left:0;width:276px;text-align:center;font-size:8.5px;line-height:17.5px;color:var(--ink)}
.pill{position:absolute;border-radius:20px;display:flex;align-items:center;justify-content:center;font-size:11px;white-space:nowrap}
.pill--dark{background:var(--dark);color:var(--white)}
.pill--line{border:1.4px solid var(--ink-soft);color:var(--ink);background:var(--white)}
.media{position:absolute}
.arrow{position:absolute;width:19px;height:19px;border:1px solid var(--ink-soft);border-radius:50%;background:var(--white);display:flex;align-items:center;justify-content:center;font-size:10px;line-height:1;color:var(--ink)}
.dots{position:absolute;display:flex;gap:4px;align-items:center}
.dots i{display:block;width:6px;height:6px;border:1px solid var(--ink-soft);border-radius:50%}
.dots i:first-child{width:8px;height:8px;background:radial-gradient(var(--ink) 40%,transparent 45%)}
.feature{position:absolute;left:71px;width:134px;background:var(--white);border-radius:8px;box-shadow:0 4px 14px rgba(0,0,0,.12);text-align:center;font-size:10.5px;line-height:17px;color:var(--ink-soft);padding-top:34px}
.feature__icon{position:absolute;left:109px;width:58px;height:58px;border-radius:50%;background:var(--dark);display:flex;align-items:center;justify-content:center}
.footer-links{font-size:6.5px;line-height:12px;color:var(--white);list-style:none}
.footer-links li::before{content:"";display:inline-block;width:2px;height:2px;background:var(--white);margin:0 5px 1px 0}
.contact{position:absolute;left:12px;display:flex;gap:12px;align-items:center;color:var(--white);font-size:9px;line-height:10px}
.contact__icon{width:17px;height:17px;border:1px solid var(--white);border-radius:3px;display:flex;align-items:center;justify-content:center}
.card-chip{width:27px;height:16px;border-radius:2px}
</style>
</head>
<body>
<div class="stage">

  <section class="screen screen--shop">
    <header class="site-header a" style="left:0;top:0;width:276px;height:54px;background:var(--white)">
      <div class="brand a" style="left:8px;top:9px;width:36px;height:36px;background:var(--dark);color:var(--white);font-size:6px;font-weight:600;display:flex;align-items:center;justify-content:center">KOR-VADO</div>
      <div class="search a" style="left:71px;top:21px;width:89px;height:14px;border:1.2px solid var(--ink);border-radius:8px;font-size:5.5px;line-height:8px;padding:2px 0 0 8px">Search
        <svg class="a" style="right:4px;top:2px" width="8" height="8" viewBox="0 0 8 8"><circle cx="3.3" cy="3.3" r="2.4" fill="none" stroke="#4f545b"/><path d="M5 5l2.4 2.4" stroke="#4f545b"/></svg>
      </div>
      <svg class="a" style="left:174px;top:20px" width="60" height="14" viewBox="0 0 60 14">
        <circle cx="7" cy="7" r="6" fill="none" stroke="#3f4348" stroke-width="1.3"/><circle cx="7" cy="5.5" r="2" fill="none" stroke="#3f4348" stroke-width="1.2"/><path d="M3 11c2-3 6-3 8 0" fill="none" stroke="#3f4348" stroke-width="1.2"/>
        <path d="M21 2h13v8h-8l-3 3v-3h-2z" fill="#3f4348"/>
        <path d="M41 2h3l2 8h8l2-6h-11" fill="none" stroke="#3f4348" stroke-width="1.3"/><circle cx="47" cy="12.5" r="1.2" fill="#3f4348"/><circle cx="53" cy="12.5" r="1.2" fill="#3f4348"/>
      </svg>
      <svg class="a" style="left:253px;top:22px" width="15" height="11" viewBox="0 0 15 11"><path d="M0 1h15M0 5.5h15M0 10h15" stroke="#4f545b" stroke-width="1.3"/></svg>
    </header>

    <section class="hero a" style="left:0;top:54px;width:276px;height:182px;background:linear-gradient(90deg,#f1f2f4 0%,#e9ebee 60%,#d6d9de 100%)">
      <div class="media" role="img" aria-label="Woman in a light coat wearing a patterned scarf" style="left:154px;top:0;width:122px;height:182px;background:linear-gradient(160deg,#cfd3d9 0%,#e3d9d6 45%,#b9928a 75%,#ded2cf 100%)"></div>
      <h1 class="a" style="left:8px;top:23px;width:180px;font-family:'Cormorant Garamond',serif;font-weight:500;text-transform:uppercase;font-size:18px;line-height:21px;letter-spacing:.2px;color:var(--ink)">Handmade unique pieces for women with style</h1>
      <p class="a" style="left:8px;top:97px;width:152px;font-size:7.5px;line-height:10.5px">Each KOR-VADO scarf is one of a kind – carefully crafted to add personality to your outfit.</p>
      <div class="pill pill--dark" style="left:8px;top:141px;width:115px;height:26px;font-size:10px">Discover Scarves&nbsp;&nbsp;↗</div>
    </section>

    <section class="why a" style="left:0;top:236px;width:276px;height:651px;background:var(--white)">
      <h2 class="heading" style="top:25px;font-family:'Cormorant Garamond',serif;text-transform:uppercase;font-size:19px">Why KOR-VADO</h2>
      <div class="rule" style="left:74px;top:51px;width:128px"></div>
      <div class="feature" style="top:108px;height:77px">Handmade locally<br>in Switzerland</div>
      <div class="feature__icon" style="top:78px"><svg width="32" height="28" viewBox="0 0 32 28" fill="none" stroke="#fff" stroke-width="1.4"><path d="M16 22c-4-3-7-6-7-9a3.5 3.5 0 017-1 3.5 3.5 0 017 1c0 3-3 6-7 9z"/><path d="M3 12v8l6 6M29 12v8l-6 6"/></svg></div>
      <div class="feature" style="top:235px;height:77px">Only 1–3 pieces<br>per design</div>
      <div class="feature__icon" style="top:206px"><svg width="30" height="30" viewBox="0 0 30 30" fill="none" stroke="#fff" stroke-width="1.4"><rect x="12" y="3" width="14" height="14"/><rect x="8" y="8" width="14" height="14"/><rect x="4" y="13" width="14" height="14"/><circle cx="11" cy="19" r="1.5"/></svg></div>
      <div class="feature" style="top:364px;height:78px">High-quality fabrics<br>without scratching</div>
      <div class="feature__icon" style="top:335px"><svg width="30" height="30" viewBox="0 0 30 30" fill="none" stroke="#fff" stroke-width="1.4"><circle cx="15" cy="10" r="6"/><circle cx="15" cy="10" r="3"/><path d="M5 20h20v6H5zM8 23h14"/></svg></div>
      <div class="feature" style="top:498px;height:77px">Lightweight and suitable<br>for everyday use</div>
      <div class="feature__icon" style="top:468px"><svg width="30" height="30" viewBox="0 0 30 30" fill="none" stroke="#fff" stroke-width="1.4"><path d="M5 10c5-4 10 4 20-2M5 16c5-4 10 4 20-2M5 22c5-4 10 4 20-2"/></svg></div>
    </section>

    <section class="story a" style="left:0;top:887px;width:276px;height:554px;background:var(--paper)">
      <div class="media" role="img" aria-label="Hands holding a softly printed fabric" style="left:27px;top:42px;width:193px;height:198px;border-radius:70px 0 0 0;background:linear-gradient(140deg,#f4e7dc 0%,#e8b08e 40%,#d99a7b 60%,#f3ece6 100%)"></div>
      <div class="media" role="img" aria-label="Light knit top with scarf on a dress form" style="left:145px;top:149px;width:118px;height:146px;border-radius:0 0 60px 0;background:linear-gradient(180deg,#ffffff 0%,#efe7dc 50%,#ffffff 100%)"></div>
      <h2 class="heading" style="top:323px">Story</h2>
      <div class="rule" style="left:108px;top:350px;width:60px"></div>
      <p class="copy" style="top:375px">Fabrics have been part of my life since childhood.<br>My grandmother and my mother created with their<br>hands – and this is exactly what I continue today.<br>I consciously take my time for each piece…</p>
      <div class="pill pill--dark" style="left:58px;top:474px;width:160px;height:38px;font-size:13px">View NEW Pieces&nbsp;&nbsp;↗</div>
    </section>

    <section class="products a" style="left:0;top:1441px;width:276px;height:563px;background:var(--mist)">
      <h2 class="heading" style="top:29px">Products</h2>
      <div class="rule" style="left:92px;top:56px;width:92px"></div>
      <div class="pill pill--line" style="left:15px;top:83px;width:78px;height:22px">New</div>
      <div class="pill pill--line" style="left:98px;top:83px;width:78px;height:22px">Scarves</div>
      <div class="pill pill--line" style="left:182px;top:83px;width:79px;height:22px">Heads</div>
      <div class="pill pill--line" style="left:60px;top:116px;width:78px;height:23px">Children</div>
      <div class="pill pill--dark" style="left:147px;top:116px;width:78px;height:23px;box-shadow:0 0 0 1.5px var(--white),0 0 0 2.5px var(--ink-soft)">All products</div>
      <article class="product-card a" style="left:61px;top:183px;width:154px;height:258px;background:var(--white);border-radius:10px;box-shadow:0 4px 14px rgba(0,0,0,.1)">
        <div class="media" role="img" aria-label="Cream knit top with triangular scarf" style="left:5px;top:6px;width:144px;height:164px;border:1px solid #ccc;border-radius:10px;background:linear-gradient(180deg,#e9e6e1 0%,#f1ece2 45%,#e6dccb 100%)"></div>
        <p class="a" style="left:0;top:181px;width:154px;text-align:center;font-size:9.5px;line-height:14px;color:var(--ink-soft)">Mira triangular scarf<br>CHF 39.00</p>
        <div class="pill pill--dark" style="left:45px;top:219px;width:64px;height:17px;font-size:7px">Add To Cart</div>
      </article>
      <div class="arrow" style="left:23px;top:307px">‹</div>
      <div class="arrow" style="left:232px;top:307px">›</div>
      <div class="dots" style="left:115px;top:458px"><i></i><i></i><i></i><i></i><i></i></div>
      <div class="pill pill--line" style="left:70px;top:502px;width:136px;height:31px;font-size:11px;border-width:1.6px">View All Products&nbsp;&nbsp;↗</div>
    </section>
  </section>

  <section class="screen screen--story">
    <section class="creation a" style="left:0;top:0;width:276px;height:463px;background:var(--paper)">
      <h2 class="heading" style="top:38px">Creation</h2>
      <div class="rule" style="left:94px;top:64px;width:88px"></div>
      <p class="copy" style="top:80px">Each scarf begins with carefully selected fabrics.<br>Colors, patterns and details are combined to create<br>a unique piece</p>
      <div class="media" role="img" aria-label="Floral printed fabric in pink, green and beige" style="left:16px;top:163px;width:191px;height:205px;border-radius:70px 0 0 0;background:linear-gradient(135deg,#d9c4a8 0%,#c98aa5 35%,#8fb3a3 65%,#d7c29f 100%)"></div>
      <div class="media" role="img" aria-label="Woman wearing a red patterned headscarf" style="left:140px;top:274px;width:122px;height:150px;border-radius:0 0 55px 0;background:linear-gradient(180deg,#c9cdd3 0%,#b24a44 45%,#3b2e2c 100%)"></div>
    </section>

    <section class="lifestyle a" style="left:0;top:463px;width:276px;height:179px">
      <div class="media" role="img" aria-label="Two women in yellow and red outfits wearing silk scarves outdoors" style="left:0;top:0;width:276px;height:179px;background:linear-gradient(90deg,#3f5a55 0%,#d9c27a 30%,#5a6d6a 50%,#b52a2a 75%,#5b6d6a 100%)"></div>
      <p class="a" style="left:0;top:141px;width:276px;text-align:center;color:var(--white);font-size:8.5px;line-height:12.5px;font-weight:500;text-shadow:0 1px 2px rgba(0,0,0,.6)">Whether in everyday life, at the office or on a walk – KOR-VADO<br>scarves bring color and lightness to any outfit.</p>
    </section>

    <section class="uniqueness a" style="left:0;top:642px;width:276px;height:195px;background:var(--paper)">
      <div class="a" style="left:8px;top:40px;width:260px;height:114px;background:var(--white);border-radius:8px;box-shadow:0 2px 8px rgba(0,0,0,.08)"></div>
      <div class="a" style="left:16px;top:48px;width:246px;height:100px;border:1px solid var(--line);border-radius:8px"></div>
      <div class="media" role="img" aria-label="Floral scarf draped over a dark leather jacket" style="left:178px;top:45px;width:84px;height:108px;background:linear-gradient(180deg,#e7e0dc 0%,#c65458 40%,#5b3a30 70%,#4a3128 100%)"></div>
      <h3 class="a" style="left:22px;top:59px;font-family:'Cormorant SC',serif;font-weight:500;font-size:19px;color:var(--ink)">Uniqueness</h3>
      <div class="a" style="left:24px;top:87px;width:73px;height:1px;background:var(--line)"></div>
      <div class="a" style="left:22px;top:85px;width:4px;height:4px;background:var(--line);transform:rotate(45deg)"></div>
      <p class="a" style="left:23px;top:97px;width:135px;font-size:8.5px;line-height:13.5px">Only 1 to 3 scarves are made from each fabric. Once sold, it remains unique</p>
    </section>

    <section class="testimonials a" style="left:0;top:837px;width:276px;height:298px;background:var(--mist)">
      <h2 class="heading" style="left:-12px;top:40px">Testimonials</h2>
      <div class="rule" style="left:70px;top:67px;width:124px"></div>
      <article class="a" style="left:53px;top:123px;width:170px;height:104px;background:var(--white);box-shadow:0 4px 14px rgba(0,0,0,.12)">
        <div class="a" style="left:128px;top:2px;font-family:'Cormorant Garamond',serif;font-size:60px;line-height:50px;color:#dcdcdc">“</div>
        <p class="a" style="left:0;top:23px;width:170px;text-align:center;font-size:8.5px;color:var(--ink)">Lena Marbach</p>
        <p class="a" style="left:0;top:34px;width:170px;text-align:center;font-size:6px;color:#e6a420;letter-spacing:1px">★★★★★</p>
        <p class="a" style="left:8px;top:49px;width:154px;text-align:center;font-family:'Cormorant Garamond',serif;font-style:italic;font-size:7.5px;line-height:11.5px">Lorem ipsum dolor sit amet, conse ctetuer adipi scing elit. Aenean comodo ligula eget doloraenean massa.<br><b style="font-style:normal;font-weight:600">I always receive compliments!</b></p>
      </article>
      <div class="media" role="img" aria-label="Portrait of the customer" style="left:120px;top:101px;width:34px;height:34px;border-radius:50%;border:2px solid var(--white);background:linear-gradient(180deg,#9fb0b3,#d7b89a)"></div>
      <div class="arrow" style="left:20px;top:166px">‹</div>
      <div class="arrow" style="left:237px;top:166px">›</div>
      <div class="dots" style="left:115px;top:257px"><i></i><i></i><i></i><i></i><i></i></div>
    </section>

    <section class="newsletter a" style="left:0;top:1135px;width:276px;height:382px;background:var(--white)">
      <h2 class="heading" style="top:33px">Newsletter Signup</h2>
      <div class="rule" style="left:92px;top:59px;width:92px"></div>
      <p class="copy" style="top:75px;line-height:11px">Find out when new models are released and<br>where you can meet KOR-VADO in person. I also</p>
      <div class="a" style="left:26px;top:119px;width:225px;height:24px;border-radius:12px;background:var(--white);box-shadow:0 1px 5px rgba(0,0,0,.18);font-size:7.5px;line-height:10px;padding:7px 0 0 13px">Enter Your Email Address
        <svg class="a" style="right:7px;top:5px" width="14" height="14" viewBox="0 0 14 14"><circle cx="7" cy="7" r="7" fill="#3f4348"/><path d="M3.5 7h7M8 4.5L10.5 7 8 9.5" fill="none" stroke="#fff" stroke-width="1.2"/></svg>
      </div>
      <div class="media" role="img" aria-label="Silk scarf in blue and pink tones" style="left:38px;top:171px;width:96px;height:114px;background:linear-gradient(135deg,#e9469a 0%,#7fb5d8 40%,#b8a3d6 70%,#e5408e 100%)"></div>
      <div class="media" role="img" aria-label="Ochre and blue patterned scarf" style="left:143px;top:171px;width:96px;height:114px;background:linear-gradient(135deg,#c8a65c 0%,#6f9bb0 50%,#c4a35e 100%)"></div>
      <div class="dots" style="left:115px;top:305px"><i></i><i></i><i></i><i></i><i></i></div>
    </section>

    <footer class="site-footer a" style="left:0;top:1517px;width:276px;height:263px;background:var(--dark)"></footer>
    <div class="a" style="left:0;top:1469px;width:276px;height:48px;background:var(--white)"></div>
    <div class="cta a" style="left:21px;top:1469px;width:235px;height:96px;border-radius:8px;background:var(--chip);overflow:hidden">
      <div class="media" role="img" aria-label="Smiling woman wearing a teal knit scarf" style="left:148px;top:0;width:87px;height:96px;background:linear-gradient(180deg,#b7c3c9 0%,#e2c3a8 40%,#6f9a98 75%,#2e2f33 100%)"></div>
      <div class="pill" style="left:21px;top:30px;width:113px;height:43px;border:1.3px solid var(--white);color:var(--white);font-size:13px;line-height:15px;text-align:center;white-space:normal">Discover<br>Scarves Now</div>
    </div>
    <div class="contact" style="top:1590px"><span class="contact__icon"><svg width="9" height="9" viewBox="0 0 9 9"><path d="M2 1l1.5 1.5-1 1a5 5 0 003 3l1-1L8 7 7 8C4 8 1 5 1 2z" fill="none" stroke="#fff" stroke-width=".9"/></svg></span><span>CALL US<br>8012 345 6789</span></div>
    <div class="contact" style="top:1621px"><span class="contact__icon"><svg width="9" height="7" viewBox="0 0 9 7"><rect x=".5" y=".5" width="8" height="6" fill="#fff"/></svg></span><span>EMAIL US<br>info@websitename.com</span></div>
    <div class="contact" style="top:1652px"><span class="contact__icon"><svg width="8" height="10" viewBox="0 0 8 10"><path d="M4 9.5S1 6 1 4a3 3 0 016 0c0 2-3 5.5-3 5.5z" fill="none" stroke="#fff"/><circle cx="4" cy="4" r="1" fill="#fff"/></svg></span><span>Address line Dummy Here<br>Address line Here</span></div>
    <ul class="footer-links a" style="left:16px;top:1688px">
      <li>Seek</li><li>General terms and conditions of business</li><li>Data protection</li><li>Imprint</li><li>Shipping Conditions</li><li>Refunds</li><li>Privacy Settings</li>
    </ul>
    <div class="legal a" style="left:0;top:1780px;width:276px;height:72px;background:var(--strip)">
      <p class="a" style="left:21px;top:10px;font-size:7px;color:var(--ink-soft)">Copyright © 2026 All Rights Reserved By Company</p>
      <div class="a" style="left:23px;top:28px;display:flex;gap:8px">
        <span class="card-chip" style="background:#2f7bd6"></span>
        <span class="card-chip" style="background:#fff;border:1px solid #ccc"></span>
        <span class="card-chip" style="background:#fff;border:1px solid #ccc"></span>
        <span class="card-chip" style="background:#3e8fb8"></span>
        <span class="card-chip" style="background:#fff;border:1px solid #ccc"></span>
      </div>
      <div class="a" style="left:23px;top:55px;display:flex;gap:8px">
        <span style="width:11px;height:11px;border:1px solid var(--ink-soft)"></span>
        <span style="width:11px;height:11px;border:1px solid var(--ink-soft)"></span>
      </div>
    </div>
  </section>

</div>
</body>
</html>
```